Wedding Decor and Entertianment business card

Company - We run a weddings and events company called Amber Finch, we provide most entertainment and decor services to our customers.

Initial idea is ....
A simple business card with logo on the front, this will be spot varnish. On a matt black background.
The reverse will be simple contact information.

But happy to try things outside of the box and would welcome some crazy ideas.

Target Market(s)

wedding couples - 21 - 40
High end wedding venues.

Industry/Entity Type

Wedding

Contact Information for Business Card

01492 718 263
amberfinchevents.co.uk
rowan@amberfinchevents.co.uk
or
helena@amberfinchevents.co.uk

Requirements
Nice to have
• black matt background with spot varnish logo on the front.

```html
<!DOCTYPE html>
<html lang="en">
<head>
<meta charset="utf-8">
<title>Amber Finch — Business Card</title>
<link href="https://fonts.googleapis.com/css2?family=Jost:wght@400&family=Roboto:wght@300&display=swap" rel="stylesheet">
<style>
  :root {
    --page: #ffffff;
    --card: #000000;
    --silver: #b9b9bc;
    --text: #f2f2f2;
    --dot-grey: #8a8a8a;
  }
  html, body {
    margin: 0;
    padding: 0;
    width: 1200px;
    height: 1200px;
    overflow: hidden;
    background: var(--page);
  }
  .canvas {
    position: relative;
    width: 1200px;
    height: 1200px;
  }
  .card {
    position: absolute;
    left: 255px;
    width: 691px;
    height: 383px;
    background: var(--card);
    overflow: hidden;
  }
  .card--front { top: 176px; }
  .card--back { top: 636px; }

  .brand {
    position: absolute;
    left: 85px;
    top: 126px;
    display: flex;
    align-items: center;
    gap: 28px;
  }
  .brand__mark {
    width: 54px;
    height: 54px;
    border-radius: 50%;
    background: var(--silver);
  }
  .brand__name {
    font-family: "Jost", sans-serif;
    font-weight: 400;
    font-size: 38px;
    letter-spacing: 0.36em;
    text-transform: uppercase;
    color: var(--silver);
    white-space: nowrap;
    line-height: 1;
  }

  .burst {
    position: absolute;
    left: 277px;
    width: 405px;
    height: 271px;
  }
  .card--front .burst { top: 112px; }
  .card--back .burst { top: 112px; }
  .burst svg { display: block; width: 100%; height: 100%; }

  .contact {
    position: absolute;
    left: 85px;
    top: 120px;
    margin: 0;
    padding: 0;
    list-style: none;
    font-family: "Roboto", sans-serif;
    font-weight: 300;
    font-size: 25px;
    line-height: 35.5px;
    color: var(--text);
    z-index: 1;
  }
</style>
</head>
<body>
  <div class="canvas">
    <section class="card card--front">
      <div class="burst">
        <svg viewBox="0 0 405 271" role="img" aria-label="Swirling tunnel of grey dots radiating from a point at the right">
          <defs>
            <radialGradient id="burst-front" cx="0.62" cy="0.55" r="0.55">
              <stop offset="0" stop-color="var(--dot-grey)" stop-opacity="0.55"/>
              <stop offset="0.6" stop-color="var(--dot-grey)" stop-opacity="0.25"/>
              <stop offset="1" stop-color="var(--dot-grey)" stop-opacity="0"/>
            </radialGradient>
          </defs>
          <rect width="405" height="271" fill="url(#burst-front)"/>
        </svg>
      </div>
      <div class="brand">
        <span class="brand__mark"></span>
        <span class="brand__name">Amber Finch</span>
      </div>
    </section>

    <section class="card card--back">
      <div class="burst">
        <svg viewBox="0 0 405 271" role="img" aria-label="Swirling tunnel of grey dots radiating from a point at the right">
          <defs>
            <radialGradient id="burst-back" cx="0.62" cy="0.55" r="0.55">
              <stop offset="0" stop-color="var(--dot-grey)" stop-opacity="0.55"/>
              <stop offset="0.6" stop-color="var(--dot-grey)" stop-opacity="0.25"/>
              <stop offset="1" stop-color="var(--dot-grey)" stop-opacity="0"/>
            </radialGradient>
          </defs>
          <rect width="405" height="271" fill="url(#burst-back)"/>
        </svg>
      </div>
      <ul class="contact">
        <li class="contact__phone">01492 718 263</li>
        <li class="contact__web">amberfinchevents.co.uk</li>
        <li class="contact__email">helena@amberfinchevents.co.uk</li>
      </ul>
    </section>
  </div>
</body>
</html>
```